Unternehmen für Ordnung und Sauberkeit am Arbeitsplatz und Produkte zur Produktionsoptimierung benötigt Visitenkarten und Briefpapier
Zielgruppe
Produkte für Ordnung und Sauberkeit am Arbeitsplatz, Organisation von Arbeitsplätzen, Produkte zur Vereinfachung von Arbeitsabläufen, Produkte zur Produktionsoptimierung unter dem Lean Gedanke, Schlagwort: "5S", nachhaltig, sauber
Aufgabenstellung
Wir sind auf der Suche nach Visitenkarten und Briefpapier für das Unternehmen taVork. Nachhaltig, Sauber usw.. Unser Firmenlogo finden Sie anbei.

```html
<!DOCTYPE html>
<html lang="de">
<head>
<meta charset="utf-8">
<title>taVork – Visitenkarte</title>
<link rel="stylesheet" href="https://fonts.googleapis.com/css2?family=Source+Sans+3:wght@400;600;700&display=swap">
<style>
  :root {
    --backdrop: #2a2a2a;
    --card-white: #ffffff;
    --brand-green: #1e8541;
    --text-dark: #1c1c1c;
    --text-mid: #2e2e2e;
    --on-green: #f4f1f1;
  }
  * { margin: 0; padding: 0; box-sizing: border-box; }
  html, body {
    width: 1163px;
    height: 1200px;
    overflow: hidden;
    background: var(--backdrop);
    font-family: "Source Sans 3", Arial, sans-serif;
  }
  .card {
    position: absolute;
    width: 698px;
    height: 400px;
  }
  .card--front {
    left: 177px;
    top: 202px;
    background: var(--card-white);
  }
  .card--back {
    left: 293px;
    top: 675px;
    background: var(--brand-green);
  }
  .brand {
    position: absolute;
    display: flex;
    align-items: center;
    gap: 14px;
    font-weight: 700;
    letter-spacing: -0.5px;
    line-height: 1;
  }
  .brand--front {
    left: 70px;
    top: 160px;
    font-size: 68px;
    color: var(--brand-green);
  }
  .brand--front .brand-square {
    width: 40px;
    height: 40px;
    background: var(--brand-green);
  }
  .brand--back {
    left: 50%;
    top: 50%;
    transform: translate(-50%, -50%);
    font-size: 72px;
    color: var(--on-green);
  }
  .brand--back .brand-square {
    width: 44px;
    height: 44px;
    background: var(--on-green);
  }
  .person {
    position: absolute;
    right: 52px;
    top: 66px;
    text-align: right;
  }
  .person-name {
    font-size: 21px;
    font-weight: 700;
    color: var(--text-dark);
  }
  .person-role {
    margin-top: 6px;
    font-size: 16px;
    color: var(--text-mid);
  }
  .contact {
    position: absolute;
    right: 26px;
    width: 320px;
    list-style: none;
  }
  .contact li {
    display: flex;
    justify-content: flex-end;
    align-items: center;
    gap: 12px;
    font-size: 17px;
    line-height: 23px;
    color: var(--text-mid);
  }
  .contact .icon {
    width: 14px;
    height: 14px;
    flex: none;
  }
  .contact .icon-blank { width: 14px; flex: none; }
  .contact--address { top: 186px; }
  .contact--web { top: 256px; }
  .contact--phone { top: 324px; }
</style>
</head>
<body>

<section class="card card--front" aria-label="Visitenkarte Vorderseite">
  <div class="brand brand--front">
    <span class="brand-square"></span>
    <span class="brand-name">taVork</span>
  </div>

  <div class="person">
    <p class="person-name">Jonas Feldberg</p>
    <p class="person-role">Geschäftsführer</p>
  </div>

  <ul class="contact contact--address">
    <li>Lindenweg 19
      <svg class="icon" viewBox="0 0 14 14" aria-hidden="true"><path d="M7 0.5a4.5 4.5 0 0 0-4.5 4.5c0 3.3 4.5 8.5 4.5 8.5s4.5-5.2 4.5-8.5A4.5 4.5 0 0 0 7 .5zm0 6.3a1.8 1.8 0 1 1 0-3.6 1.8 1.8 0 0 1 0 3.6z" fill="#1e8541"/></svg>
    </li>
    <li>79312 Emmerau <span class="icon-blank"></span></li>
  </ul>

  <ul class="contact contact--web">
    <li>info@feldweg.de
      <svg class="icon" viewBox="0 0 14 14" aria-hidden="true"><rect x="1" y="3" width="12" height="8" fill="#1e8541"/><path d="M1 3l6 4.5L13 3" fill="none" stroke="#fff" stroke-width="1"/></svg>
    </li>
    <li>www.feldweg.de
      <svg class="icon" viewBox="0 0 14 14" aria-hidden="true"><g fill="none" stroke="#1e8541" stroke-width="1.2"><circle cx="7" cy="7" r="5.5"/><ellipse cx="7" cy="7" rx="2.3" ry="5.5"/><path d="M1.5 7h11"/></g></svg>
    </li>
  </ul>

  <ul class="contact contact--phone">
    <li>0 31 47 / 26 58 13
      <svg class="icon" viewBox="0 0 14 14" aria-hidden="true"><path d="M1 5c0-1.5 2.7-2.5 6-2.5S13 3.5 13 5v1.2H10V4.8H4v1.4H1zM3 7h8l1.5 4.5h-11z" fill="#1e8541"/></svg>
    </li>
    <li>0 31 47 / 26 58 140
      <svg class="icon" viewBox="0 0 14 14" aria-hidden="true"><path d="M3.5 1.5h5v3h-5zM1.5 5h11v6.5h-11zM3.5 11h7v1.5h-7z" fill="#1e8541"/></svg>
    </li>
  </ul>
</section>

<section class="card card--back" aria-label="Visitenkarte Rückseite">
  <div class="brand brand--back">
    <span class="brand-square"></span>
    <span class="brand-name">taVork</span>
  </div>
</section>

</body>
</html>
```